Cover art needed for best LASIK patient education book ever written!

Help us design a an outstanding cover for this book:
Clear Sight Ahead?
Hidden Truths for Picking a Trustworthy Refractive Specialist
By Walter B. Hensley, MD and
Derek T. Oswalt
We give you nine chapters of easy-to-understand explanations about how LASIK may, or may not, help improve you vision. In addition, we offer tell-all secrets and insider tips on how to tell whether the LASIK center is doing what is best for your vision, or for their financial performance. If you have ever considered LASIK laser vision correction, this book is required reading before you make a decision.
So what do you say? Will you draw a great cover for our book? By the way, preferred colors include jewel tones like deep purple and royal blue.
Requirements
Must have
- Book Title
- Subtitle
- Outstanding Graphics
- Walter B. Hensley, MD (main author) should be in slightly larger font than Derek T. Oswalt (secondary author)
- compelling art that makes you want to pick up the book
Should not have
- no blood, image representing pain, or anything else that would generally not appeal to patients

```html
<!DOCTYPE html>
<html lang="en">
<head>
<meta charset="utf-8">
<title>Clear Sight Ahead? — Book Cover</title>
<link rel="stylesheet" href="https://fonts.googleapis.com/css2?family=Raleway:wght@300;400&family=Roboto+Condensed:wght@400&display=swap">
<style>
  :root {
    --page-bg: #e6e8ea;
    --cover-top: #d4eef8;
    --cover-mid: #bfe3f3;
    --cover-bottom: #ece6f6;
    --ink-dark: #1a1a1f;
    --ink-grey: #3a3a44;
    --jewel-purple: #8a2a8c;
    --deep-purple: #5b2a86;
    --royal-blue: #2b3a9e;
    --magenta: #a2306a;
    --iris-blue: #8fd3f0;
    --amber: #c79055;
  }
  html, body {
    margin: 0;
    padding: 0;
    width: 1200px;
    height: 1200px;
    overflow: hidden;
    background: var(--page-bg);
  }
  .cover {
    position: absolute;
    left: 219px;
    top: 30px;
    width: 762px;
    height: 1140px;
    overflow: hidden;
    background: linear-gradient(180deg, var(--cover-top) 0%, var(--cover-mid) 45%, #dcecf7 75%, var(--cover-bottom) 100%);
  }
  .cover-backdrop {
    position: absolute;
    inset: 0;
    background:
      radial-gradient(ellipse 420px 300px at 62% 34%, rgba(120,170,210,0.35), transparent 70%),
      radial-gradient(ellipse 300px 500px at 8% 60%, rgba(140,200,230,0.35), transparent 70%);
  }
  .title {
    position: absolute;
    top: 82px;
    left: 0;
    width: 100%;
    margin: 0;
    text-align: center;
    font-family: "Raleway", sans-serif;
    font-weight: 300;
    font-size: 66px;
    letter-spacing: -1px;
    color: var(--ink-dark);
  }
  .title .accent { font-weight: 400; }
  .emblem-art {
    position: absolute;
    left: 80px;
    top: 250px;
    width: 600px;
    height: 640px;
    background:
      radial-gradient(ellipse 150px 110px at 50% 46%, var(--iris-blue) 0%, rgba(199,144,85,0.75) 60%, transparent 100%),
      radial-gradient(ellipse 300px 320px at 50% 48%, var(--deep-purple) 0%, var(--royal-blue) 55%, rgba(91,42,134,0.5) 80%, transparent 100%);
  }
  .subtitle {
    position: absolute;
    top: 890px;
    left: 0;
    width: 100%;
    margin: 0;
    text-align: center;
    font-family: "Roboto Condensed", sans-serif;
    font-weight: 400;
    color: var(--jewel-purple);
    line-height: 1.1;
  }
  .subtitle .lead { display: block; font-size: 30px; }
  .subtitle .main { display: block; font-size: 37px; margin-top: 8px; }
  .authors {
    position: absolute;
    top: 1012px;
    left: 0;
    width: 100%;
    text-align: center;
    font-family: "Roboto Condensed", sans-serif;
    color: var(--ink-grey);
  }
  .author-primary { display: block; font-size: 28px; }
  .author-primary .small { font-size: 22px; }
  .author-secondary { display: block; font-size: 22px; margin-top: 4px; }
</style>
</head>
<body>
  <main class="cover">
    <div class="cover-backdrop" role="img" aria-label="Faint photographic backdrop of an eye and a diagnostic screen in light blue tones"></div>

    <h1 class="title">CLEAR <span class="accent">SIGHT</span> AHEAD?</h1>

    <div class="emblem-art" role="img" aria-label="Comma-shaped emblem in purple and royal blue framing a close-up photograph of a blue eye"></div>

    <p class="subtitle">
      <span class="lead">HIDDEN TRUTHS FOR PICKING A</span>
      <span class="main">TRUSTWORTHY REFRACTIVE SPECIALIST</span>
    </p>

    <div class="authors">
      <span class="author-primary"><span class="small">BY</span> WALTER B. HENSLEY, MD <span class="small">AND</span></span>
      <span class="author-secondary">DEREK T. OSWALT</span>
    </div>
  </main>
</body>
</html>
```